Radon Reduction & Mold Removal Website

I need you to set up a WordPress account for me and design a full width, professional-looking, mobile-responsive website for my business. We offer radon reduction and mold removal (two household environmental issues).
We have merged 2 companies and need a single website to promote both services (radon and mold). Here are the current websites from the 2 businesses that have merged:
RADON
http://klendor-airfix.com/
MOLD
http://brisketfungusclear.net/
Once complete, I will need the login to the WordPress account so I have access to the site to make changes, additions, and modifications.
Target Market(s)
Home Owners
Industry/Entity Type
Home And Garden
Look and feel
Each slider illustrates characteristics of the customer's brand and the style your logo design should communicate.

```html
<!DOCTYPE html>
<html lang="en">
<head>
<meta charset="utf-8">
<title>Klendor Environmental – Radon Mitigation &amp; Mold Removal</title>
<link href="https://fonts.googleapis.com/css2?family=Lato:wght@400;700;900&display=swap" rel="stylesheet">
<style>
:root{
  --green:#6fb82f;--green-dark:#3f6e17;--green-bright:#5cc42b;
  --yellow:#f5e51a;--black:#111;--dark:#1f1f1f;--orange:#f0642a;
  --cream:#fbf3e2;--text:#555;--white:#fff;--grey:#f1f1f1;
}
*{box-sizing:border-box;margin:0;padding:0}
html,body{width:1200px;height:3716px;overflow:hidden}
body{font-family:'Lato',sans-serif;color:var(--text);background:var(--white);font-size:15px;line-height:1.5}
.wrap{width:1040px;margin:0 auto;position:relative;height:100%}
section,header,footer{position:relative;overflow:hidden}
.btn-small{display:inline-block;background:var(--green);color:#fff;font-size:12px;font-weight:700;padding:4px 14px;border-radius:2px}

/* hero */
.hero{height:780px}
.hero-photo{position:absolute;inset:0;background:linear-gradient(160deg,#c9d8b0 0%,#9bb36a 35%,#d8b89a 60%,#6a8a3a 100%)}
.topbar{position:absolute;top:0;left:0;right:0;height:100px;background:rgba(10,10,10,.85);border-bottom:3px solid var(--yellow)}
.brand{position:absolute;left:80px;top:22px;display:flex;align-items:center;gap:12px}
.brand-mark{width:50px;height:50px;background:var(--yellow)}
.brand-name{color:var(--yellow);font-weight:900;font-size:24px;line-height:1.1;width:150px}
.phone{position:absolute;right:80px;top:14px;color:#fff;font-weight:700;font-size:16px;display:flex;gap:8px;align-items:center}
.nav{position:absolute;right:80px;top:54px;display:flex;gap:6px}
.nav a{color:#fff;font-weight:700;font-size:13px;padding:10px 18px;text-decoration:none}
.nav a.active{background:var(--yellow);color:var(--black)}
.hero-tag{position:absolute;left:80px;top:470px;width:400px;background:rgba(20,40,5,.85);padding:18px 26px;color:var(--yellow);font-weight:900;font-size:30px;line-height:1.15;text-transform:uppercase}
.hero-note{position:absolute;left:480px;top:470px;width:640px;height:112px;background:rgba(0,0,0,.75);color:var(--yellow);font-size:13px;padding:18px 24px}

/* what we do */
.whatwedo{height:380px;background:var(--green)}
.section-title{text-align:center;font-size:32px;font-weight:700;color:#fff;padding-top:18px}
.wwd-boxes{display:flex;gap:40px;margin-top:18px}
.wwd-box{flex:1;background:#fff;height:230px;padding:14px 22px;position:relative}
.wwd-box h3{font-weight:400;font-size:28px;color:#333;margin-bottom:8px}
.wwd-box p{font-size:12px;line-height:1.45}
.wwd-box .btn-small{position:absolute;right:20px;bottom:12px}
.wwd-foot{display:flex;justify-content:space-around;color:#1d3a05;font-weight:700;font-size:20px;margin-top:16px}

/* services */
.services{height:650px;background:#fff}
.services .section-title{color:var(--green);font-weight:400;font-size:36px;padding-top:40px}
.svc-row{display:flex;gap:40px;margin-top:80px}
.svc-card{flex:1;background:var(--cream);height:400px;padding:70px 28px 20px;position:relative;text-align:left}
.svc-icon{position:absolute;top:-40px;left:50%;margin-left:-40px;width:80px;height:80px;border-radius:50%;background:#fff;border:3px solid var(--orange);display:flex;align-items:center;justify-content:center}
.svc-card h3{text-align:center;color:var(--orange);font-size:22px;font-weight:700;line-height:1.2;margin-bottom:24px}
.svc-card li{font-size:13px;margin:0 0 14px 16px}
.svc-card .btn-small{position:absolute;left:50%;transform:translateX(-50%);bottom:22px;background:var(--orange)}

/* cta */
.cta{height:150px}
.cta-row{display:flex;align-items:center;gap:20px;padding-top:20px}
.cta-btn{flex:1;height:100px;background:var(--green-bright);color:#fff;font-size:36px;display:flex;align-items:center;justify-content:center;border-radius:4px}
.cta-or{width:70px;height:70px;border-radius:50%;background:var(--orange);color:#fff;font-weight:700;font-size:20px;display:flex;align-items:center;justify-content:center}

/* mold */
.mold{height:650px}
.mold h2{text-align:center;font-size:32px;font-weight:400;color:#333;padding-top:40px}
.mold-row{display:flex;gap:80px;margin-top:60px;padding:0 40px}
.mold-card{flex:1;border:1px solid #ddd;height:420px;padding:16px;position:relative;background:#fff}
.mold-photo{height:210px;background:linear-gradient(180deg,#b8cce0,#d7cfb8 60%,#7a9a4a)}
.mold-card p{font-size:12px;margin-top:16px;line-height:1.45}
.mold-card .btn-small{position:absolute;right:16px;bottom:16px}

/* about */
.about{height:270px;background:var(--grey)}
.about-photo{position:absolute;left:0;top:30px;width:320px;height:210px;background:linear-gradient(135deg,#9a8c7a,#d4c6b0)}
.about-info{position:absolute;left:360px;top:10px;right:0}
.about-contacts{display:flex;gap:30px;font-size:12px;font-weight:700;color:#333}
.about-contacts span{display:flex;gap:6px;align-items:center}
.about-contacts i{display:inline-block;width:16px;height:16px;background:var(--green)}
.about h2{font-size:36px;font-weight:400;color:#333;margin:22px 0 10px}
.about p{font-size:12.5px}

/* testimonials */
.testimonials{height:350px}
.testimonials h2{text-align:center;color:var(--orange);font-size:30px;font-weight:400;padding-top:30px}
.t-row{display:flex;gap:60px;margin-top:50px;padding:0 60px;position:relative}
.t-item{flex:1;display:flex;gap:20px}
.t-photo{width:120px;height:140px;flex:none;background:linear-gradient(180deg,#cfc3b5,#8b8277)}
.t-item p{font-size:12.5px}
.t-item strong{display:block;margin-top:14px;color:#333}
.t-arrow{position:absolute;top:50px;width:26px;height:26px;background:var(--orange)}
.t-arrow.left{left:0}.t-arrow.right{right:0}

/* footer */
.footer{height:410px;background:var(--dark);color:#bbb;border-top:4px solid var(--yellow)}
.foot-cols{display:flex;gap:60px;padding-top:40px}
.foot-col{font-size:13px}
.foot-col h4{color:#fff;font-size:15px;margin:16px 0 8px}
.foot-col a{display:block;color:#bbb;text-decoration:none;line-height:1.7}
.foot-brand{display:flex;align-items:center;gap:10px}
.socials{display:flex;gap:8px;margin-top:10px}
.socials i{width:26px;height:26px;border-radius:50%;background:var(--yellow);display:block}
.newsletter input{display:block;width:280px;height:30px;border:0;margin-bottom:8px;background:#fff}
.subscribe{background:var(--yellow);color:#111;font-weight:700;padding:6px 20px;display:inline-block;font-size:13px}
.quote-btn{display:inline-block;margin-top:40px;background:var(--orange);color:#fff;font-weight:700;font-size:18px;padding:12px 30px}
.bottombar{height:76px;background:#000;color:#888;font-size:11px}
.bottombar .wrap{display:flex;justify-content:space-between;padding-top:10px}
.badges{position:absolute;left:50%;transform:translateX(-50%);bottom:10px;display:flex;gap:14px}
.badges i{display:block;width:34px;height:28px;background:#444;border-radius:4px}
</style>
</head>
<body>

<header class="hero">
  <div class="hero-photo" role="img" aria-label="Family of four smiling together outdoors on a sunny lawn"></div>
  <div class="topbar">
    <div class="brand"><div class="brand-mark"></div><div class="brand-name">Klendor Environmental</div></div>
    <div class="phone">
      <svg width="16" height="16" viewBox="0 0 24 24"><path fill="#fff" d="M6.6 10.8a15 15 0 0 0 6.6 6.6l2.2-2.2a1 1 0 0 1 1-.25 11.4 11.4 0 0 0 3.6.6 1 1 0 0 1 1 1V20a1 1 0 0 1-1 1A17 17 0 0 1 3 4a1 1 0 0 1 1-1h3.5a1 1 0 0 1 1 1c0 1.25.2 2.45.57 3.57a1 1 0 0 1-.25 1z"/></svg>
      1-800-555-0148
    </div>
    <nav class="nav"><a class="active">HOME</a><a>SERVICES</a><a>PRODUCTS</a><a>CONTACT US</a><a>GET A QUOTE</a></nav>
  </div>
  <div class="hero-tag">Keep your family healthy, safe, and radon free</div>
  <div class="hero-note">Klendor Environmental is the best choice for radon mitigation services for your home or business. Radon is the number one cause of lung cancer among non-smokers and is responsible for about 21,000 lung cancer deaths.</div>
</header>

<section class="whatwedo">
  <div class="wrap">
    <h2 class="section-title">What We Do</h2>
    <div class="wwd-boxes">
      <div class="wwd-box"><h3>Radon Mitigation Services</h3><p>We test every home for radon and design a reduction system that fits its foundation, soil and layout. Our certified crews seal cracks, install vent piping and quiet fans, then retest to confirm lower levels. Most systems are fitted within a single day with minimal disruption, and every job comes with a written warranty and follow-up testing plan so your family can breathe easy for years to come.</p><span class="btn-small">Read More</span></div>
      <div class="wwd-box"><h3>Rapid Mold Removal</h3><p>Our mold specialists locate moisture sources, contain affected rooms and remove growth from walls, attics and basements. We use safe treatments and air scrubbers to clean the space, then help you fix leaks and ventilation so mold does not return. Each project includes a clear inspection report, before and after photos and advice on keeping humidity low throughout the seasons ahead.</p><span class="btn-small">Read More</span></div>
    </div>
    <div class="wwd-foot"><span>Fix Your Home Today</span><span>Call Us : 1-800-555-0148</span></div>
  </div>
</section>

<section class="services">
  <div class="wrap">
    <h2 class="section-title">Our Services</h2>
    <div class="svc-row">
      <div class="svc-card">
        <div class="svc-icon"><svg width="36" height="36" viewBox="0 0 24 24"><path fill="none" stroke="#f0642a" stroke-width="2" d="M3 11l9-7 9 7v9H3z M9 20v-6h6v6"/></svg></div>
        <h3>Residential<br>Services</h3>
        <ul><li>Our team has mitigated more homes than any other company.</li><li>Over 100,000 radon systems installed nationwide.</li><li>Same day and next day service available.</li></ul>
        <span class="btn-small">Read More</span>
      </div>
      <div class="svc-card">
        <div class="svc-icon"><svg width="36" height="36" viewBox="0 0 24 24"><path fill="none" stroke="#f0642a" stroke-width="2" d="M4 21V4h9v17 M13 9h7v12 M2 21h20 M7 8h3M7 12h3M7 16h3"/></svg></div>
        <h3>Commercial<br>Services</h3>
        <ul><li>We follow your state and local mitigation standards.</li><li>Our environmental engineers design custom solutions for each site.</li><li>Experienced with offices, warehouses and manufacturing buildings.</li></ul>
        <span class="btn-small">Read More</span>
      </div>
      <div class="svc-card">
        <div class="svc-icon"><svg width="36" height="36" viewBox="0 0 24 24"><path fill="none" stroke="#f0642a" stroke-width="2" d="M12 21s-7-7-7-12a7 7 0 0 1 14 0c0 5-7 12-7 12z"/><circle cx="12" cy="9" r="2.5" fill="none" stroke="#f0642a" stroke-width="2"/></svg></div>
        <h3>Real Estate<br>Services</h3>
        <ul><li>Time matters when a home sale is on the line.</li><li>Agents rely on us to meet their closing dates.</li><li>Our founder is a former realtor.</li></ul>
        <span class="btn-small">Read More</span>
      </div>
    </div>
  </div>
</section>

<section class="cta">
  <div class="wrap">
    <div class="cta-row"><div class="cta-btn">Call Us:1-800-555-0148</div><div class="cta-or">OR</div><div class="cta-btn">Get a Quote Now!</div></div>
  </div>
</section>

<section class="mold">
  <div class="wrap">
    <h2>Michigan Mold Remediation Specialists</h2>
    <div class="mold-row">
      <div class="mold-card"><div class="mold-photo" role="img" aria-label="House exterior with mold removal label"></div><p>Our mold removal professionals are trained in safe cleanup and moisture control. Mold can harm people with allergies and asthma, so we act quickly.</p><span class="btn-small">Read More</span></div>
      <div class="mold-card"><div class="mold-photo" role="img" aria-label="Home with radon system label"></div><p>Our radon team shares the same guidance on reducing airborne toxins. We use proven methods and modern equipment for every home.</p><span class="btn-small">Read More</span></div>
      <div class="mold-card"><div class="mold-photo" role="img" aria-label="Brick family home exterior"></div><p>We hold the licenses and certifications needed to test for radon and mold, and our inspectors can assess any home quickly.</p><span class="btn-small">Read More</span></div>
    </div>
  </div>
</section>

<section class="about">
  <div class="wrap">
    <div class="about-photo" role="img" aria-label="Technician installing a radon vent system"></div>
    <div class="about-info">
      <div class="about-contacts"><span><i></i>1-800-555-0148</span><span><i></i>Mon – Sat 8am – 6pm</span><span><i></i>hello@klendorenv.com</span></div>
      <h2>About Klendor Environmental</h2>
      <p>Klendor Environmental is quickly becoming a household name across the United States. Offering radon reduction for over forty locations across America, we have a reputation as the leader in radon mitigation. We were founded with a small team and a single truck and have grown through honest work, fair prices and care for every family we serve.</p>
    </div>
  </div>
</section>

<section class="testimonials">
  <div class="wrap">
    <h2>What our happy customers has to say</h2>
    <div class="t-row">
      <span class="t-arrow left"></span>
      <div class="t-item"><div class="t-photo" role="img" aria-label="Portrait of a customer"></div><div><p>“The crew arrived on time, explained every step and our radon levels dropped right away. Great service from start to finish.”</p><strong>Dale Fenwick</strong></div></div>
      <div class="t-item"><div class="t-photo" role="img" aria-label="Portrait of a customer"></div><div><p>“They found the source of our basement mold and cleaned it fast. The house smells fresh again and we feel safe.”</p><strong>Ruth Calloway</strong></div></div>
      <span class="t-arrow right"></span>
    </div>
  </div>
</section>

<footer class="footer">
  <div class="wrap">
    <div class="foot-cols">
      <div class="foot-col" style="width:360px">
        <div class="foot-brand"><div class="brand-mark" style="width:40px;height:40px;background:var(--yellow)"></div><div class="brand-name">Klendor Environmental</div></div>
        <h4>Corporate Headquarters</h4>
        <a>Office: 1-800-555-0148</a><a>Fax: 1-800-555-0149</a><a>Mon – Fri 8am – 6pm</a><a>Sat 9am – 2pm</a>
      </div>
      <div class="foot-col" style="width:240px">
        <h4>Navigation</h4><a>Home</a><a>Services</a><a>Products</a><a>Contact Us</a><a>Get a Quote</a>
        <h4>Follow Us</h4><div class="socials"><i></i><i></i><i></i><i></i><i></i></div>
      </div>
      <div class="foot-col newsletter">
        <h4>Klendor Newsletter</h4><input aria-label="Name"><input aria-label="Email"><span class="subscribe">Subscribe</span><br>
        <span class="quote-btn">Get a Quote Now ›</span>
      </div>
    </div>
  </div>
</footer>

<div class="bottombar" style="position:relative">
  <div class="wrap"><span>Copyright © 2024 Klendor Environmental Mitigation Services</span><span>Terms of Use · Privacy Policy · Directions</span></div>
  <div class="badges"><i></i><i></i><i></i><i></i><i></i><i></i><i></i></div>
</div>

</body>
</html>
```